Clothing range for the petite modern mature woman needs a card design

We need a business card design for a new Sydney based company called lark reed. We provide clothing to the modern mature woman who finds it difficult to source clothes that do not make them look frumpy or do not fit. We have an idea we would like an apple with the peel unravelling and possibly the silhouette of a woman's body coming out of the peel. The lark reed represents the womans body shape and dressing it.

Target Market(s)

modern mature aged woman

Industry/Entity Type

Clothing

Contact Information for Business Card

abn: 41270386915
will provide email at a later date
a spiel re clothes for modern woman???

Font styles to use
Serif
Sans Serif

Requirements
Must have
• will need name - ABN -will need email address but still working on that (TBA)
Nice to have
• picture of an apple with its peel coming off and possibly the silhouette of a woman coming out. the issue a lot of women in the over 50 range have is that the clothing is very dated or makes the woman frumpy. we are providing clothes for the woman who has difficulty in finding fashionable clothes in their size.
Should not have
• don't want childlike

```html
<!DOCTYPE html>
<html lang="en">
<head>
<meta charset="utf-8">
<title>lark reed — business card</title>
<link rel="stylesheet" href="https://fonts.googleapis.com/css2?family=Raleway:wght@300;400&display=swap">
<style>
  :root {
    --leaf: #8cc63f;
    --blush: #f2c2ad;
    --paper: #ffffff;
    --edge: #d9d9d9;
    --canvas: #ffffff;
  }
  * { box-sizing: border-box; margin: 0; padding: 0; }
  html, body {
    width: 1200px; height: 1200px; overflow: hidden;
    background: var(--canvas);
    font-family: "Raleway", "Helvetica Neue", Arial, sans-serif;
    font-weight: 300;
  }
  .canvas { position: relative; width: 1200px; height: 1200px; }

  .card {
    position: absolute; top: 147px;
    width: 544px; height: 309px;
    background: var(--paper);
    border: 1px solid var(--edge);
  }
  .card--front { left: 36px; }
  .card--back { left: 616px; }

  .card__band {
    position: absolute; top: 0; bottom: 0; width: 20px;
    background: var(--leaf);
  }
  .card__band--left { left: 0; }
  .card__band--right { right: 0; }

  .brand { position: absolute; text-align: center; }
  .brand__dot { display: block; margin: 0 auto; border-radius: 50%; background: var(--leaf); }
  .brand__name {
    display: block; color: var(--blush);
    text-transform: uppercase; letter-spacing: 0.12em; font-weight: 300;
    white-space: nowrap;
  }

  .card--front .brand { left: 0; right: 0; top: 70px; }
  .card--front .brand__dot { width: 140px; height: 140px; }
  .card--front .brand__name { margin-top: 42px; font-size: 27px; }

  .card--back .brand { left: 44px; top: 36px; width: 120px; }
  .card--back .brand__dot { width: 70px; height: 70px; }
  .card--back .brand__name { margin-top: 14px; font-size: 15px; }

  .contact__name {
    position: absolute; right: 42px; top: 104px;
    color: var(--leaf); font-size: 21px; letter-spacing: 0.06em; font-weight: 400;
    text-transform: uppercase; white-space: nowrap;
  }
  .contact__role {
    position: absolute; right: 42px; top: 134px;
    color: var(--blush); font-size: 17px; letter-spacing: 0.03em; white-space: nowrap;
  }
  .contact__details {
    position: absolute; right: 42px; top: 204px; text-align: right;
    color: var(--leaf); font-size: 13px; line-height: 19px; font-style: normal;
    white-space: nowrap;
  }
</style>
</head>
<body>
<main class="canvas">

  <section class="card card--front" aria-label="Business card front">
    <div class="card__band card__band--left"></div>
    <div class="card__band card__band--right"></div>
    <div class="brand">
      <span class="brand__dot"></span>
      <span class="brand__name">Lark Reed</span>
    </div>
  </section>

  <section class="card card--back" aria-label="Business card back">
    <div class="card__band card__band--right"></div>
    <div class="brand">
      <span class="brand__dot"></span>
      <span class="brand__name">Lark Reed</span>
    </div>
    <h1 class="contact__name">Derya Kaplan</h1>
    <p class="contact__role">Store Manager</p>
    <address class="contact__details">
      14 Palmer St, Sydney NSW<br>
      +61 2 5550 4837<br>
      derya@larkreed.com<br>
      ABN 41270386915
    </address>
  </section>

</main>
</body>
</html>
```